Website Design for Law Firm

We need a fresh new website design for our client 'Vendrick Legal' who specialises as a Criminal, Traffic & Civil Lawyer in Perth, Western Australia. We are looking for a very clean, professional and elegant look for the website, a presence of power and class needed as he deals with high end clients. Black, Silver and hints of gold need to run through the design without making the site look too dark. We are after a very modern, spacious web look, use of large readable text with links to social media (such as Chatterloom, Zumbly+, Quibbr, WorkMesh) to stand out and his contact details to be made very predominate.

Reason: Public holidays here in Australia, need more business hours to discuss designs with client.

Reason: Client needs more time to look through designs.

Reason: Client is going over last of designs. Design will be picked early next week!

Industry/Entity Type

Law Firm

```html
<!DOCTYPE html>
<html lang="en">
<head>
<meta charset="utf-8">
<title>Vendrick Legal — Criminal, Traffic &amp; Civil Lawyer, Perth WA</title>
<link rel="stylesheet" href="https://fonts.googleapis.com/css2?family=Roboto:wght@300;400;500;700&display=swap">
<style>
  :root{
    --brown-deep:#4a2a20;
    --brown-nav:#3d2219;
    --heading:#4a2a20;
    --orange:#f0a23b;
    --text:#5a5a5a;
    --panel:#e4e1de;
    --tab:#7b7b7b;
    --footer:#3a3a3a;
    --footer-dark:#2b2b2b;
    --footer-row:#444444;
    --bar:#0f0f0f;
    --white:#ffffff;
    --case-title:#6a2c14;
  }
  *{box-sizing:border-box;margin:0;padding:0}
  html,body{width:1200px;height:2542px;overflow:hidden;background:#fff}
  body{font-family:"Roboto",Arial,sans-serif;color:var(--text);position:relative}
  .page{position:relative;width:1200px;height:2542px;overflow:hidden}
  .abs{position:absolute}

  /* Hero */
  .hero{left:0;top:0;width:1200px;height:561px;overflow:hidden}
  .hero-photo{position:absolute;inset:0;
    background:
      radial-gradient(ellipse at 78% 40%, rgba(230,200,150,.55) 0%, rgba(0,0,0,0) 40%),
      radial-gradient(ellipse at 20% 30%, rgba(240,160,70,.6) 0%, rgba(0,0,0,0) 45%),
      linear-gradient(180deg,#b8652a 0%,#8e4418 45%,#5e2a10 100%);}
  .brand{left:200px;top:36px;font-weight:700;font-size:30px;color:#1c120d;letter-spacing:.5px;display:flex;align-items:center;gap:10px}
  .brand-mark{width:22px;height:22px;background:#1c120d}
  .nav{left:488px;top:36px;width:512px;height:45px;background:var(--brown-nav);display:flex;align-items:center;justify-content:space-around;padding:0 6px}
  .nav a{color:var(--white);text-decoration:none;font-size:11px;font-weight:500}
  .hero-title{left:198px;top:265px;color:var(--white);font-size:24px;font-weight:400;line-height:39px;text-shadow:0 1px 2px rgba(0,0,0,.3)}
  .arrow{top:256px;width:47px;height:55px;background:rgba(20,10,5,.75);display:flex;align-items:center;justify-content:center}
  .arrow-left{left:0}
  .arrow-right{right:0}
  .dots{left:589px;top:531px;display:flex;gap:6px}
  .dots span{width:11px;height:11px;border-radius:50%;background:#fff;border:2px solid #555}
  .dots span.on{background:#333}

  /* Intro */
  .section-title{width:1200px;left:0;text-align:center;color:var(--heading);font-size:25px;font-weight:400}
  .copy{left:212px;width:776px;text-align:center;font-size:11px;line-height:24.5px;color:var(--text)}

  /* Practice areas */
  .practice{left:0;top:1003px;width:1200px;height:417px;background:var(--brown-deep)}
  .practice .section-title{color:var(--white);top:26px}
  .practice-sub{left:0;width:1200px;top:70px;text-align:center;color:var(--white);font-size:12px;font-weight:500}
  .tabs{left:200px;top:114px;width:800px;height:42px;background:var(--tab);display:flex}
  .tab{height:42px;display:flex;align-items:center;justify-content:center;color:#fff;font-size:12px;border-right:1px solid #9a9a9a}
  .tab.active{background:var(--orange)}
  .tab-panel{left:200px;top:156px;width:800px;height:216px;background:var(--panel)}
  .list{position:absolute;top:32px;list-style:none}
  .list li{font-size:12px;color:#3a3a3a;height:24px;display:flex;align-items:center;gap:10px}
  .list li::before{content:"";width:0;height:0;border-left:6px solid var(--orange);border-top:5px solid transparent;border-bottom:5px solid transparent}
  .list-left{left:18px}
  .list-right{left:435px}

  /* Testimonials */
  .testimonials{left:0;top:1420px;width:1200px;height:278px}
  .testimonials-bg{position:absolute;inset:0;background:radial-gradient(ellipse at 50% 40%,#3a4a55 0%,#253139 55%,#1a2228 100%)}
  .testimonials .section-title{color:var(--white);top:40px}
  .quote{left:290px;top:105px;width:620px;text-align:center;color:#fff;font-size:12px;line-height:24px}
  .quote-mark{top:98px;color:#fff;font-size:30px;font-family:Georgia,serif;line-height:1}
  .quote-author{left:0;width:1200px;top:177px;text-align:center;color:var(--orange);font-size:12px}
  .sq-dots{left:561px;top:231px;display:flex;gap:6px}
  .sq-dots span{width:11px;height:11px;background:#111}
  .sq-dots span.on{background:var(--orange)}

  /* Recent cases */
  .case{position:absolute;width:395px;height:122px}
  .case-thumb{position:absolute;left:0;top:0;width:183px;height:122px}
  .case-body{position:absolute;left:195px;top:0;width:190px}
  .case-title{font-size:10.5px;font-weight:700;color:var(--case-title);line-height:19px}
  .case-text{font-size:10.5px;color:#666;line-height:19px;margin-top:4px}
  .case-by{font-size:10.5px;color:#222;line-height:19px;font-weight:500}

  /* Footer */
  .footer{left:0;top:2098px;width:1200px;height:368px;background:var(--footer)}
  .footer-title{color:#fff;font-size:20px;font-weight:400;top:46px}
  .info{left:200px;top:73px;width:254px}
  .info-row{height:34px;background:var(--footer-row);display:flex;align-items:center;color:#fff;font-size:12px;gap:12px}
  .info-icon{width:34px;height:34px;background:var(--orange);display:flex;align-items:center;justify-content:center;flex:none}
  .info-about{background:var(--footer-dark);height:134px;padding:16px 16px 0 46px;color:#888;font-size:12px;line-height:18px;font-weight:300}
  .socials{display:grid;grid-template-columns:1fr 1fr;gap:5px;margin-top:12px;margin-left:-20px}
  .socials span{height:20px;background:#4c5f78;color:#fff;font-size:10px;display:flex;align-items:center;justify-content:center}
  .field{position:absolute;border:1px solid #8a8a8a;border-radius:3px;color:#9a9a9a;font-size:11px;padding:0 10px;display:flex;align-items:center;justify-content:space-between}
  .field.area{align-items:flex-start;padding-top:9px}
  .send{left:475px;top:307px;width:517px;height:34px;background:var(--orange);color:#fff;font-size:12px;display:flex;align-items:center;justify-content:center;border-radius:2px}
  .bottom-bar{left:0;top:2466px;width:1200px;height:76px;background:var(--bar)}
  .copyright{left:200px;top:31px;color:#ddd;font-size:11px}
</style>
</head>
<body>
<div class="page">

  <!-- Hero -->
  <header class="abs hero">
    <div class="hero-photo" role="img" aria-label="Photograph of brass scales of justice in a warmly lit courtroom"></div>
    <div class="abs brand"><span class="brand-mark"></span>Vendrick Legal</div>
    <nav class="abs nav">
      <a href="#">Home</a><a href="#">About Us</a><a href="#">Practice Area</a><a href="#">Testimonials</a><a href="#">Recent Cases</a><a href="#">Contact Us</a>
    </nav>
    <h1 class="abs hero-title">Criminal Defence Lawyer, Traffic Defence Lawyer &amp;<br>Civil Litigation Lawyer, Perth WA</h1>
    <div class="abs arrow arrow-left"><svg width="16" height="22" viewBox="0 0 16 22"><path d="M12 2 3 11l9 9" fill="none" stroke="#fff" stroke-width="4"/></svg></div>
    <div class="abs arrow arrow-right"><svg width="16" height="22" viewBox="0 0 16 22"><path d="M4 2l9 9-9 9" fill="none" stroke="#fff" stroke-width="4"/></svg></div>
    <div class="abs dots"><span class="on"></span><span></span><span></span></div>
  </header>

  <!-- Welcome -->
  <h2 class="abs section-title" style="top:586px">Welcome To Vendrick Legal</h2>
  <p class="abs copy" style="top:624px">Vendrick Legal is an established law firm practicing in Criminal Law, Traffic Law and Civil Law. We are conveniently located close to the Perth Magistrates Court and District Court. We understand that facing legal proceedings is very daunting and our clients are always saying "we don't know what to expect, we haven't been through anything like this before". We provide easytounderstand advice and expert assistance to help you navigate complex court procedures. Our legal fees are open and transparent so you know from day one how much your legal defence is going to cost. We service all metropolitan courts as well as providing a visiting service to Karratha and Port Hedland Our office hours are 8:30 5:00 pm Monday to Friday but appointments can be madeoutside of these times.</p>

  <!-- About -->
  <h2 class="abs section-title" style="top:764px">About Us</h2>
  <div class="abs copy" style="top:803px">
    <p>Vendrick Legal is an established Law firm specialising in Criminal Law, Traffic Law and Civil Law. Dr Marcus Vendrick is the firm's Legal Practitioner Director.</p>
    <p>Marcus is an experienced Legal Advocate dedicated to protecting you legal rights. In the last two years he has notched up over 2,000 appearances in the Magistrates Court, District Court, Supreme Court and Children's Court. Marcus was formerly with the Public Defence Commission of WA Criminal Division and before that he enjoyed a long and successful international career with various agencies of the Allied Nations Council. He has taught Criminal Law and Advanced Criminal Law at University level. He is a member of the Defence Counsel Guild and Southern Advocates Alliance.</p>
    <p>Marcus offers a wealth of legal and negotiating experience to help you with your legal problems and deal with police and prosecuting authorities such as State and Federal DPP and Federal, State and Local government agencies.</p>
  </div>

  <!-- Practice Areas -->
  <section class="abs practice">
    <h2 class="abs section-title">Practice Areas</h2>
    <p class="abs practice-sub">We practice across a wide range of legal areas. A few common areas where we can provide you with competent legal representation are:</p>
    <div class="abs tabs">
      <div class="tab active" style="width:137px">Criminal Law</div>
      <div class="tab" style="width:93px">Traffic Law</div>
      <div class="tab" style="width:85px">Civil Law</div>
      <div class="tab" style="width:123px">Special Applications</div>
      <div class="tab" style="width:119px">Breaching Offences</div>
      <div class="tab" style="width:85px">Court Work</div>
    </div>
    <div class="abs tab-panel">
      <ul class="list list-left">
        <li>Criminal law</li><li>Armed robbery</li><li>Stealing/burglary</li><li>Fraud including commonwealth offences</li><li>Serious assaults and wounding</li><li>Sex offences</li>
      </ul>
      <ul class="list list-right">
        <li>Sexual penetration</li><li>Indecent dealing</li><li>Drug offences</li><li>Weapons offences</li><li>Property confiscation under proceeds of crime laws</li><li>Murder/manslaughter</li>
      </ul>
    </div>
  </section>

  <!-- Testimonials -->
  <section class="abs testimonials">
    <div class="testimonials-bg" role="img" aria-label="Dark blue-grey textured backdrop"></div>
    <h2 class="abs section-title">Testimonals</h2>
    <span class="abs quote-mark" style="left:254px">&ldquo;</span>
    <p class="abs quote">I was lucky to be one of the first to use Lumora theme, I used other review style themes in the past, but none of them were as solid, effective and good looking as this one. Now this theme is all I use for my review sites DORIAN PELL</p>
    <span class="abs quote-mark" style="left:932px">&rdquo;</span>
    <p class="abs quote-author">- Tessa Marlow</p>
    <div class="abs sq-dots"><span class="on"></span><span></span><span></span></div>
  </section>

  <!-- Recent Cases -->
  <h2 class="abs section-title" style="top:1721px">Recent Cases</h2>

  <article class="case" style="left:200px;top:1776px">
    <div class="case-thumb" role="img" aria-label="Photograph of old law books and a gavel" style="background:linear-gradient(135deg,#c98a3a,#6a3510)"></div>
    <div class="case-body">
      <h3 class="case-title">Indecent Assault Childrens Court - charges dropped after negotiations with police</h3>
      <p class="case-text">Praesent augue arcu, ornare ut tincidunt eu, mattis a libero. Pellentesque habitant morbi tristique senectus et netus et</p>
      <p class="case-by">by Northgate Studio | 23 May 2014</p>
    </div>
  </article>
  <article class="case" style="left:605px;top:1776px">
    <div class="case-thumb" role="img" aria-label="Photograph of a gavel resting on a printed document" style="background:linear-gradient(135deg,#e0b565,#8a5a22)"></div>
    <div class="case-body" style="left:200px">
      <h3 class="case-title">Indecent Assault Childrens Court - charges dropped after negotiations with police</h3>
      <p class="case-text">Praesent augue arcu, ornare ut tincidunt eu, mattis a libero. Pellentesque habitant morbi tristique senectus et netus et</p>
      <p class="case-by">by Northgate Studio | 23 May 2014</p>
    </div>
  </article>
  <article class="case" style="left:200px;top:1944px">
    <div class="case-thumb" role="img" aria-label="Photograph of a wooden courtroom bench" style="background:linear-gradient(135deg,#b0774a,#4a2212)"></div>
    <div class="case-body">
      <h3 class="case-title">Indecent Assault Childrens Court - charges dropped after negotiations with police</h3>
      <p class="case-text">Praesent augue arcu, ornare ut tincidunt eu, mattis a libero. Pellentesque habitant morbi tristique senectus et netus et</p>
      <p class="case-by">by Northgate Studio | 23 May 2014</p>
    </div>
  </article>
  <article class="case" style="left:605px;top:1944px">
    <div class="case-thumb" role="img" aria-label="Photograph of a money bag with a dollar sign" style="background:linear-gradient(135deg,#d8d2c8,#5a5550)"></div>
    <div class="case-body" style="left:200px">
      <h3 class="case-title">Indecent Assault Childrens Court - charges dropped after negotiations with police</h3>
      <p class="case-text">Praesent augue arcu, ornare ut tincidunt eu, mattis a libero. Pellentesque habitant morbi tristique senectus et netus et</p>
      <p class="case-by">by Northgate Studio | 23 May 2014</p>
    </div>
  </article>

  <!-- Footer -->
  <footer class="abs footer">
    <h2 class="abs footer-title" style="left:200px">Information</h2>
    <h2 class="abs footer-title" style="left:475px">Contact Us</h2>

    <div class="abs info">
      <div class="info-row">
        <span class="info-icon"><svg width="16" height="16" viewBox="0 0 16 16"><rect x="3" y="2" width="10" height="13" fill="none" stroke="#fff" stroke-width="1.6"/><path d="M6 5h1M9 5h1M6 8h1M9 8h1M7 15v-3h2v3" stroke="#fff" stroke-width="1.4"/></svg></span>Company
      </div>
      <div class="info-about">
        Lorem ipsum dolor sit amet, consectetuer adipiscing elit. Morbi commodo.
        <div class="socials"><span>Chatterloom</span><span>Quibbr</span><span>WorkMesh</span><span>Zumbly+</span></div>
      </div>
      <div class="info-row">
        <span class="info-icon"><svg width="14" height="18" viewBox="0 0 14 18"><path d="M7 17s6-6.5 6-10.5A6 6 0 0 0 1 6.5C1 10.5 7 17 7 17z" fill="#fff"/><circle cx="7" cy="6.5" r="2.2" fill="#f0a23b"/></svg></span>Address
      </div>
      <div class="info-row">
        <span class="info-icon"><svg width="16" height="16" viewBox="0 0 16 16"><path d="M3 1l3 3-1.5 2a9 9 0 0 0 5.5 5.5L12 10l3 3-2 2C7 15 1 9 1 3z" fill="#fff"/></svg></span>Phone
      </div>
      <div class="info-row">
        <span class="info-icon"><svg width="16" height="12" viewBox="0 0 16 12"><rect x="1" y="1" width="14" height="10" fill="none" stroke="#fff" stroke-width="1.4"/><path d="M1 1l7 6 7-6" fill="none" stroke="#fff" stroke-width="1.4"/></svg></span>Email
      </div>
    </div>

    <div class="field" style="left:475px;top:73px;width:247px;height:34px">Your Name
      <svg width="12" height="12" viewBox="0 0 12 12"><circle cx="6" cy="3.5" r="3" fill="#9a9a9a"/><path d="M0 12c0-4 3-5 6-5s6 1 6 5z" fill="#9a9a9a"/></svg>
    </div>
    <div class="field" style="left:744px;top:73px;width:248px;height:34px">Your Email
      <svg width="14" height="10" viewBox="0 0 14 10"><rect x="1" y="1" width="12" height="8" fill="none" stroke="#9a9a9a" stroke-width="1.2"/><path d="M1 1l6 5 6-5" fill="none" stroke="#9a9a9a" stroke-width="1.2"/></svg>
    </div>
    <div class="field area" style="left:475px;top:122px;width:517px;height:170px">Insert your message
      <svg width="12" height="12" viewBox="0 0 12 12"><path d="M1 11l1-3 6-6 2 2-6 6z" fill="#9a9a9a"/></svg>
    </div>
    <div class="abs send">SEND</div>
  </footer>

  <div class="abs bottom-bar">
    <p class="abs copyright">© 2014 Vendrick All Rights Reserved</p>
  </div>
</div>
</body>
</html>
```